KestavLaw a fully remote and fully bilingual law firm for the Florida injured

1. Can you describe what your company does?- a solo lawyer practice in Florida, D.C., and soon in NY. I offer services for auto accidents, negligence, boat accident, motorcycle accident, insurance claims, premises liability, and things of the like.

2. Who are your target customers for the website? Drivers, passengers, pedestrians involved in accidents where they were injured and need help making a claim against the other vehicle or insurance company- throughout the entire state of Florida, but primarily in greater central florida area for english speaking and latino community offering a 100% bilingual services ENGLISH/SPANISH and 100% remote, where I wont make clients come to an office ever, and will private online meetings, signing portals, and all to have it efficient for clients benefit.

3. Do you have an existing domain name / website address? yes, kestavlaw.example through Bramblefield Suite. i need help in getting in brought to you so you can handle it please.

4. In addition to a Home Page, which other pages / sections would you like your website to have:
About Us
Contact Us
Products / Services
Office / Mailing Address
Testimonials / Reviews
FAQs
Terms and Conditions
Any other page / section you would like- DO EVERYTHING IN BOTH LANGUAGES- ENGLISH AND SPANISH
I want the page to have a way for people to calendar appts with me. and also
to make transactions - accepting all methods of payment

For each of the pages / sections you’d like to have, please provide the text (and images, if available) you would like to include.

5. Which of the below are features and functionalities your website will need:
Image Gallery
Videos
Contact Form
Mailing List
Maps
FAQs
Accepting payments / donations
6. Please provide the URLs for the social media profiles you'd like to link to the website. I have none, I am just starting, I actually want to have the online presence ready before my official launch.

Target Market(s)

Injured individuals by the negligent act of another in Florida

Industry/Entity Type

LAWYER/ AUTO ACCIDENT/NEGLIGENCE/ PREMISES LIABILITY/ CIVIL LAW

Coding

Coded - Design and coding required

Number of Pages Required

1 page

Requirements
Must have
• bilingual ENGLISH and SPANISH; a button for people to calendar appointments with me; accept payments, and to be able to integrate with major software like quillseal, pinnex, etc since I need to integrate under the fully remote platform
Nice to have
• look at my logo from markforge.example it has the Dellacorte Law and KestavLaw.example together.. I have the kestavlaw.example domain from Bramblefield. need you guys to help integrate that too , meaning to be able to use that domain for my website.

```html
<!DOCTYPE html>
<html lang="en">
<head>
<meta charset="utf-8">
<title>KestavLaw — Remote Bilingual Injury Law</title>
<link rel="stylesheet" href="https://fonts.googleapis.com/css2?family=Poppins:wght@400;500;600;700&family=Open+Sans:ital,wght@0,400;0,600;1,400&family=Yellowtail&display=swap">
<style>
:root{
  --navy:#233080;
  --navy-deep:#1c2670;
  --red:#d3302f;
  --ink:#2b2b2b;
  --muted:#6b6f7a;
  --soft:#eef0f6;
  --line:#e3e5ec;
  --footer:#222326;
  --white:#ffffff;
}
*{box-sizing:border-box;margin:0;padding:0}
html,body{width:1200px;height:5172px;overflow:hidden}
body{font-family:"Open Sans",Arial,sans-serif;color:var(--ink);background:var(--white);position:relative}
h1,h2,h3,h4,.btn,.nav,.brand-name{font-family:"Poppins",Arial,sans-serif}
.btn{display:inline-flex;align-items:center;gap:8px;background:var(--red);color:var(--white);font-weight:600;font-size:16px;text-transform:uppercase;border-radius:30px;padding:0 30px;height:58px;letter-spacing:.2px}
.brand{display:flex;align-items:center;gap:12px}
.brand-mark{width:76px;height:76px;border-radius:50%;background:var(--navy)}
.brand-name{font-weight:600;font-size:34px;color:var(--ink)}

.topbar{height:40px;background:var(--navy)}
.header{height:110px;position:relative}
.header .brand{position:absolute;left:110px;top:16px}
.contact-line{position:absolute;right:112px;top:26px;font-size:17px;font-family:"Poppins",sans-serif;display:flex;gap:20px;align-items:center}
.contact-line b{font-weight:500}
.contact-line .ico{color:var(--red)}
.lang{color:var(--red)} .lang span{color:var(--ink)}
.nav{position:absolute;right:112px;top:70px;display:flex;gap:24px;font-size:17px}

.hero{height:590px;position:relative;background:linear-gradient(180deg,#3a63b8 0%,#6f92cf 35%,#2b3a6b 70%,#18223f 100%)}
.hero h1{position:absolute;left:108px;top:90px;font-size:72px;font-weight:600;color:var(--white)}
.hero p{position:absolute;left:112px;top:200px;font-size:21px;color:var(--white)}
.hero .btn{position:absolute;left:112px;top:258px;height:56px}

.about{height:750px;background:var(--soft);position:relative}
.about .portrait{position:absolute;left:40px;top:20px;width:510px;height:730px;background:linear-gradient(180deg,#d6d9e2 0%,#8a8d95 55%,#55585f 100%)}
.about .hi{position:absolute;left:610px;top:80px;font-family:"Yellowtail",cursive;font-size:72px;color:var(--navy)}
.about h2{position:absolute;left:714px;top:172px;font-size:44px;font-weight:500}
.about .copy{position:absolute;left:610px;top:268px;width:490px;font-size:15.5px;line-height:27px;color:var(--muted)}
.about .copy p+p{margin-top:26px}
.about .btn{position:absolute;left:610px;top:592px}

.services{height:945px;position:relative}
.services h2{text-align:center;padding-top:76px;font-size:42px;font-weight:500}
.grid{position:absolute;left:110px;top:170px;width:980px;display:grid;grid-template-columns:repeat(3,1fr)}
.card{height:375px;text-align:center;padding-top:40px;border-right:2px solid var(--line)}
.card:nth-child(3n){border-right:none}
.card:nth-child(-n+3){border-bottom:2px solid var(--line)}
.card svg.icon{width:140px;height:100px}
.card h3{font-size:21px;font-weight:500;margin-top:16px}
.card p{font-size:15.5px;line-height:26px;color:var(--muted);width:275px;margin:14px auto 0}
.card .go{display:inline-flex;width:40px;height:40px;border:2px solid var(--muted);border-radius:50%;align-items:center;justify-content:center;margin-top:26px}

.remote{height:765px;background:var(--soft);position:relative}
.remote .panel{position:absolute;left:110px;top:92px;width:490px;height:573px;background:var(--navy);color:var(--white);padding:48px 52px}
.remote h2{font-size:42px;font-weight:600}
.remote .lead{font-size:15.5px;line-height:27px;margin-top:18px}
.feature{display:flex;align-items:center;gap:26px;margin-top:28px}
.feature .ring{width:92px;height:92px;border:2px solid rgba(255,255,255,.8);border-radius:50%;display:flex;align-items:center;justify-content:center}
.feature span{font-family:"Poppins",sans-serif;font-size:21px;line-height:27px;font-weight:500}
.remote .btn{margin-top:30px;height:56px}
.remote .photo{position:absolute;left:600px;top:92px;width:490px;height:573px;background:linear-gradient(135deg,#c9ccd2 0%,#8a7d72 45%,#4a5f86 100%)}

.reviews{height:780px;position:relative;text-align:center}
.reviews h2{padding-top:96px;font-size:44px;font-weight:500}
.quote{width:700px;margin:28px auto 0;font-style:italic;font-size:17.5px;line-height:32px;color:var(--muted)}
.who{margin-top:34px;font-family:"Poppins",sans-serif;font-size:21px}
.video{position:absolute;left:373px;top:396px;width:454px;height:302px;background:linear-gradient(135deg,#e2e3e6 0%,#b7aea3 50%,#6e6e72 100%);box-shadow:0 12px 30px rgba(30,40,90,.15)}
.video .play{position:absolute;left:200px;top:124px;width:52px;height:52px;border-radius:50%;background:rgba(0,0,0,.55);display:flex;align-items:center;justify-content:center}
.arrow{position:absolute;top:528px;width:40px;height:40px;border:2px solid var(--red);border-radius:50%;display:flex;align-items:center;justify-content:center}

.contact{height:740px;background:var(--soft);position:relative}
.contact .map{position:absolute;left:110px;top:96px;width:367px;height:542px;background:linear-gradient(160deg,#f3f3f3 0%,#e4e7ec 55%,#cfd9e6 100%)}
.contact .form{position:absolute;left:477px;top:96px;width:613px;height:542px;background:var(--navy);padding:44px 46px}
.form h2{color:var(--white);font-size:42px;font-weight:600}
.fields{display:grid;grid-template-columns:1fr 1fr;gap:22px 16px;margin-top:30px}
.field{background:var(--white);height:44px;font-size:15px;color:#555;padding:12px 18px}
.field.wide{grid-column:1/3;height:130px}
.form .btn{margin-top:32px;height:56px;padding:0 40px}

.footer{height:452px;background:var(--footer);color:var(--white);position:relative}
.footer .brand{position:absolute;left:110px;top:105px}
.footer .brand-mark{width:108px;height:108px}
.footer .brand-name{color:var(--white);font-size:46px;font-weight:500}
.col{position:absolute;top:66px}
.col h4{font-size:19px;font-weight:500}
.col ul{list-style:none;margin-top:16px;font-size:15.5px;line-height:30px}
.col li .ico{color:var(--red);margin-right:12px}
.footer .rule{position:absolute;left:110px;right:110px;top:350px;border-top:1px solid #44464b}
.copyright{position:absolute;left:110px;top:392px;font-size:15.5px}
.social{position:absolute;right:112px;top:376px;display:flex;gap:12px}
.social span{width:42px;height:42px;border:2px solid var(--red);border-radius:50%}
</style>
</head>
<body>

<div class="topbar"></div>

<header class="header">
  <div class="brand"><div class="brand-mark"></div><div class="brand-name">KestavLaw</div></div>
  <div class="contact-line">
    <span><span class="ico">✉</span> Email: <b>info@kestavlaw.example</b></span>
    <span><span class="ico">✆</span> Call: 1 555 010 2040</span>
    <span class="lang">EN <span>/ ES</span></span>
  </div>
  <nav class="nav"><span>About Us</span><span>Contact Us</span><span>Services</span><span>Mailing Address</span><span>Testimonials</span><span>FAQs</span></nav>
</header>

<section class="hero" role="img" aria-label="Evening city skyline with a blue bridge over the river">
  <h1>KestavLaw</h1>
  <p>A solo lawyer practice in Florida, D.C., and soon in NY.</p>
  <span class="btn"><svg width="18" height="18" viewBox="0 0 18 18" fill="none" stroke="#fff" stroke-width="2"><rect x="2" y="3" width="14" height="13"/><path d="M2 7h14M6 1v4M12 1v4"/></svg>Book an appointment</span>
</section>

<section class="about">
  <div class="portrait" role="img" aria-label="Portrait of the lawyer in a grey suit, arms crossed"></div>
  <div class="hi">Hi I am</div>
  <h2>Daniel Arvelo</h2>
  <div class="copy">
    <p>Nemo enim ipsam voluptatem quia voluptas sit aspernatur aut odit aut fugit, sed quia consequuntur magni dolores eos qui rat ione voluptatem sequi nesciunt. Neque porro quisquam est, qui dolorem ipsum quia dolor sit amet, consectetur, adipisci velit, sed quia non numquam eius modi tempora incidunt ut laboret dolore magnam aliquam quaerat voluptatem.</p>
    <p>Jma veniam, quis nostrum exercitationem ullam corporis susc ipit laboriosam, nisi ut aliquid ex ea commodi consequatu sau tem vel eum iure reprehenderit.</p>
  </div>
  <span class="btn">Contact us</span>
</section>

<section class="services">
  <h2>I offer services</h2>
  <div class="grid">
    <div class="card">
      <svg class="icon" viewBox="0 0 140 100" fill="none" stroke="#233080" stroke-width="3"><rect x="10" y="45" width="50" height="25" rx="4"/><circle cx="22" cy="72" r="7"/><circle cx="48" cy="72" r="7"/><rect x="80" y="40" width="50" height="30" rx="4"/><circle cx="92" cy="72" r="7"/><circle cx="118" cy="72" r="7"/><path d="M62 30l8 10 6-14 4 12" stroke="#d3302f"/></svg>
      <h3>Auto accidents</h3><p>Nemo enim ipsam voluptatem quia voluptas sit aspernatur aut odit aut fugi sed quia consequu.</p>
      <span class="go"><svg width="12" height="12" viewBox="0 0 12 12" fill="none" stroke="#d3302f" stroke-width="2"><path d="M4 2l4 4-4 4"/></svg></span>
    </div>
    <div class="card">
      <svg class="icon" viewBox="0 0 140 100" fill="none" stroke="#233080" stroke-width="3"><circle cx="55" cy="15" r="7"/><path d="M45 30h20v30h-4v32h-12V60h-4z"/><path d="M88 12l16 26H72z" stroke="#d3302f"/><path d="M88 22v8M88 33v1" stroke="#d3302f"/></svg>
      <h3>Negligence</h3><p>Nemo enim ipsam voluptatem quia voluptas sit aspernatur aut odit aut fugi sed quia consequu.</p>
      <span class="go"><svg width="12" height="12" viewBox="0 0 12 12" fill="none" stroke="#d3302f" stroke-width="2"><path d="M4 2l4 4-4 4"/></svg></span>
    </div>
    <div class="card">
      <svg class="icon" viewBox="0 0 140 100" fill="none" stroke="#233080" stroke-width="3"><path d="M40 60l70-45v35z" stroke="#d3302f"/><path d="M20 70c10-6 20 6 30 0s20 6 30 0 20 6 30 0M20 82c10-6 20 6 30 0s20 6 30 0 20 6 30 0"/></svg>
      <h3>Boat accident</h3><p>Nemo enim ipsam voluptatem quia voluptas sit aspernatur aut odit aut fugi sed quia consequu.</p>
      <span class="go"><svg width="12" height="12" viewBox="0 0 12 12" fill="none" stroke="#d3302f" stroke-width="2"><path d="M4 2l4 4-4 4"/></svg></span>
    </div>
    <div class="card">
      <svg class="icon" viewBox="0 0 140 100" fill="none" stroke="#233080" stroke-width="3"><circle cx="40" cy="70" r="14"/><circle cx="100" cy="70" r="14"/><path d="M40 70l25-25h20l15 25"/><path d="M60 30l8-12 6 12 8-10 4 14" stroke="#d3302f"/></svg>
      <h3>Motorcycle accident</h3><p>Nemo enim ipsam voluptatem quia voluptas sit aspernatur aut odit aut fugi sed quia consequu.</p>
      <span class="go"><svg width="12" height="12" viewBox="0 0 12 12" fill="none" stroke="#d3302f" stroke-width="2"><path d="M4 2l4 4-4 4"/></svg></span>
    </div>
    <div class="card">
      <svg class="icon" viewBox="0 0 140 100" fill="none" stroke="#233080" stroke-width="3"><path d="M45 8h40l12 12v72H45z"/><path d="M55 60h30M55 70h30M55 80h20"/><circle cx="70" cy="32" r="12" stroke="#d3302f"/><path d="M90 55l10 4v10c0 6-5 10-10 12-5-2-10-6-10-12V59z"/></svg>
      <h3>Insurance claims</h3><p>Nemo enim ipsam voluptatem quia voluptas sit aspernatur aut odit aut fugi sed quia consequu.</p>
      <span class="go"><svg width="12" height="12" viewBox="0 0 12 12" fill="none" stroke="#d3302f" stroke-width="2"><path d="M4 2l4 4-4 4"/></svg></span>
    </div>
    <div class="card">
      <svg class="icon" viewBox="0 0 140 100" fill="none" stroke="#233080" stroke-width="3"><circle cx="70" cy="45" r="13" stroke="#d3302f"/><path d="M70 8v18M40 45h16M84 45h16M48 22l10 12M92 22l-10 12"/><path d="M45 75h20l20-8c6-2 8 6 2 9l-22 12H45z"/></svg>
      <h3>Premises liability</h3><p>Nemo enim ipsam voluptatem quia voluptas sit aspernatur aut odit aut fugi sed quia consequu.</p>
      <span class="go"><svg width="12" height="12" viewBox="0 0 12 12" fill="none" stroke="#d3302f" stroke-width="2"><path d="M4 2l4 4-4 4"/></svg></span>
    </div>
  </div>
</section>

<section class="remote">
  <div class="panel">
    <h2>100% Remote</h2>
    <p class="lead">Jma veniam, quis nostrum exercitationem der ulm corporis susc ut aliquid ex ea commodi consdeequ atu saum iure reprehenderit.</p>
    <div class="feature"><div class="ring"><svg width="44" height="34" viewBox="0 0 44 34" fill="none" stroke="#fff" stroke-width="2.5"><rect x="7" y="3" width="30" height="21" rx="2"/><path d="M2 30h40"/></svg></div><span>Private<br>online meetings</span></div>
    <div class="feature"><div class="ring"><svg width="40" height="40" viewBox="0 0 40 40" fill="none" stroke="#fff" stroke-width="2.5"><rect x="4" y="8" width="26" height="28" rx="3"/><path d="M16 26l2-7 16-16 5 5-16 16z"/></svg></div><span>Signing<br>portals</span></div>
    <span class="btn">Contact us</span>
  </div>
  <div class="photo" role="img" aria-label="Client in a denim jacket working on a laptop"></div>
</section>

<section class="reviews">
  <h2>Client Reviews</h2>
  <p class="quote">“ Lorem ipsum dolor sit amet, consectetur adipiscing elit, sed do eiusmod tempor incidi dunt ut labore et dolore magna aliqua. Ut enim ad minim veniam, quis nostrud exercita tion ullamco laboris nisi ut aliquip ex ea commodo consequat. Duis aute irure dolor in reprehenderit in voluptate velit esse cillum dolore eu fug ”</p>
  <p class="who">- MARISOL</p>
  <span class="arrow" style="left:296px"><svg width="12" height="12" viewBox="0 0 12 12" fill="none" stroke="#d3302f" stroke-width="2"><path d="M8 2L4 6l4 4"/></svg></span>
  <div class="video" role="img" aria-label="Video testimonial from a smiling client"><span class="play"><svg width="18" height="18" viewBox="0 0 18 18"><path d="M5 3l10 6-10 6z" fill="#fff"/></svg></span></div>
  <span class="arrow" style="left:864px"><svg width="12" height="12" viewBox="0 0 12 12" fill="none" stroke="#d3302f" stroke-width="2"><path d="M4 2l4 4-4 4"/></svg></span>
</section>

<section class="contact">
  <div class="map" role="img" aria-label="Map of the state of Florida"></div>
  <div class="form">
    <h2>Get In Touch</h2>
    <div class="fields">
      <div class="field">First Name</div><div class="field">Last Name</div>
      <div class="field">Email</div><div class="field">Phone no.</div>
      <div class="field wide">Message</div>
    </div>
    <span class="btn">Send</span>
  </div>
</section>

<footer class="footer">
  <div class="brand"><div class="brand-mark"></div><div class="brand-name">KestavLaw</div></div>
  <div class="col" style="left:596px"><h4>Quick Links</h4>
    <ul><li>Home</li><li>About Us</li><li>Contact Us</li><li>Services</li><li>Mailing Address</li><li>Testimonials</li><li>FAQs</li></ul></div>
  <div class="col" style="left:836px"><h4>Contact Info</h4>
    <ul style="line-height:44px"><li><span class="ico">⚲</span>Florida, D.C</li><li><span class="ico">✆</span>1 555 010 2040</li><li><span class="ico">✉</span>info@kestavlaw.example</li></ul></div>
  <div class="rule"></div>
  <p class="copyright">© Copyright 2025, KestavLaw. All rights reserved.</p>
  <div class="social"><span></span><span></span></div>
</footer>

</body>
</html>
```